Riverpeak Analytics needs new design business card

We are video surveillance and analytics software development company.
I am looking for a professional business card.
Our website is www.riverpeakanalytics.example.au
Please have a loo and get the feel for who we are and what we do.
I do not know what else to give you apart from good luck and I hope your design gets selected.
Thank you very much for participating
Business
Contact Information for Business Card
Address
27/15 Marlowe Street Fernbrook NSW 2199
Telephone 1300 582 417
Mobile 0450 731 258
email: marcus@riverpeakanalytics.example.au
name
Marcus Helvard
Position
Managing Director
Font styles to use
Other font styles liked:
- Arial
Look and feel

```html
<!DOCTYPE html>
<html lang="en">
<head>
<meta charset="utf-8">
<title>Riverpeak Analytics – Business Card</title>
<link rel="stylesheet" href="https://fonts.googleapis.com/css2?family=Open+Sans:wght@400;600;700&display=swap">
<style>
  :root {
    --card-blue: #0a47f5;
    --accent-orange: #ff7a00;
    --tile-grey: #8f9c9c;
    --stripe-grey: #9a9f96;
    --brand-navy: #1f3d8f;
    --ink: #111111;
    --outline: #1a1a1a;
    --paper: #ffffff;
  }
  html, body {
    margin: 0;
    padding: 0;
    width: 1200px;
    height: 1000px;
    overflow: hidden;
    background: var(--paper);
  }
  .canvas {
    position: relative;
    width: 1200px;
    height: 1000px;
    font-family: "Open Sans", Arial, sans-serif;
  }
  .card-shapes {
    position: absolute;
    left: 0;
    top: 0;
  }
  .text {
    position: absolute;
    margin: 0;
    white-space: nowrap;
  }
  .brand {
    display: flex;
    align-items: center;
    gap: 14px;
    color: var(--brand-navy);
    font-weight: 600;
  }
  .brand-mark {
    background: var(--brand-navy);
    flex: none;
  }
  .brand-name {
    margin: 0;
    line-height: 1.12;
  }
  .front-brand { left: 297px; top: 104px; }
  .front-brand .brand-mark { width: 58px; height: 58px; }
  .front-brand .brand-name { font-size: 38px; }
  .back-brand { left: 686px; top: 668px; gap: 12px; }
  .back-brand .brand-mark { width: 40px; height: 40px; }
  .back-brand .brand-name { font-size: 31px; }

  .holder-name {
    left: 274px;
    top: 226px;
    font-size: 29px;
    font-weight: 600;
    color: var(--ink);
  }
  .holder-role {
    font-size: 14px;
    font-weight: 700;
    margin-left: 4px;
  }
  .contact-list {
    left: 274px;
    top: 285px;
    font-size: 19.5px;
    font-weight: 600;
    line-height: 27px;
    color: var(--ink);
    list-style: none;
    padding: 0;
  }
  .back-email {
    left: 274px;
    top: 690px;
    font-size: 18px;
    font-weight: 400;
    color: var(--paper);
  }
</style>
</head>
<body>
<main class="canvas">
  <svg class="card-shapes" width="1200" height="1000" viewBox="0 0 1200 1000" aria-hidden="true">
    <!-- front card -->
    <g class="front-card">
      <rect class="side-bar" x="247" y="85" width="11" height="386" fill="var(--accent-orange)" stroke="var(--outline)" stroke-width="1"/>
      <polygon class="chevron-orange" points="797,85 810,85 848,278 795,471 779,471 838,278" fill="var(--accent-orange)" stroke="var(--outline)" stroke-width="1"/>
      <polygon class="chevron-grey" points="804,85 810,85 848,278 795,471 789,471 842,278" fill="var(--stripe-grey)" stroke="var(--outline)" stroke-width="1"/>
      <polygon class="chevron-panel" points="811,85 967,85 967,471 796,471 849,278" fill="var(--card-blue)" stroke="var(--outline)" stroke-width="1.5"/>
    </g>
    <!-- back card -->
    <g class="back-card">
      <rect class="floating-tile" x="688" y="525" width="60" height="53" fill="var(--card-blue)"/>
      <polygon class="back-panel" points="252,498 768,498 642,705 830,913 252,913" fill="var(--card-blue)" stroke="var(--outline)" stroke-width="1.5"/>
      <g class="tile-grid">
        <rect x="282" y="525" width="60" height="53" fill="var(--tile-grey)"/>
        <rect x="415" y="525" width="60" height="53" fill="var(--accent-orange)"/>
        <rect x="555" y="525" width="60" height="53" fill="var(--tile-grey)"/>
        <rect x="282" y="614" width="60" height="53" fill="var(--accent-orange)"/>
        <rect x="418" y="614" width="60" height="53" fill="var(--tile-grey)"/>
        <rect x="555" y="614" width="60" height="53" fill="var(--accent-orange)"/>
        <rect x="286" y="747" width="60" height="53" fill="var(--tile-grey)"/>
        <rect x="418" y="747" width="60" height="53" fill="var(--accent-orange)"/>
        <rect x="558" y="747" width="60" height="53" fill="var(--tile-grey)"/>
        <rect x="286" y="845" width="60" height="53" fill="var(--accent-orange)"/>
        <rect x="418" y="845" width="60" height="53" fill="var(--tile-grey)"/>
        <rect x="552" y="845" width="60" height="53" fill="var(--accent-orange)"/>
        <rect x="674" y="845" width="60" height="53" fill="var(--tile-grey)"/>
      </g>
      <g class="floating-tiles" fill="var(--card-blue)">
        <rect x="884" y="525" width="61" height="53"/>
        <rect x="802" y="588" width="61" height="53"/>
        <rect x="786" y="773" width="60" height="53"/>
        <rect x="905" y="784" width="61" height="53"/>
        <rect x="865" y="860" width="61" height="53"/>
      </g>
    </g>
  </svg>

  <div class="text brand front-brand">
    <span class="brand-mark"></span>
    <p class="brand-name">Riverpeak<br>Analytics</p>
  </div>

  <p class="text holder-name">Marcus Helvard <span class="holder-role">(Position Managing Director )</span></p>

  <ul class="text contact-list">
    <li>Address 27/15 Marlowe Street Fernbrook NSW 2199</li>
    <li>Telephone -1300 582 417</li>
    <li>Mobile - 0450 731 258</li>
  </ul>

  <p class="text back-email">marcus@riverpeakanalytics.example.au</p>

  <div class="text brand back-brand">
    <span class="brand-mark"></span>
    <p class="brand-name">Riverpeak<br>Analytics</p>
  </div>
</main>
</body>
</html>
```